Business Cards - Bright Trim Yard (Cleaning, Handyman & Mowing Business)
Bright Trim Yard
Business Cards - Bright Trim Yard (Cleaning, Handyman & Mowing Business) - Trade
Creative Brief
Professional
PO Box 318 Galloway Rise, QLD, 4127
0412 GO TIDY (0412 46 8439) should these 2 versions of the number be put on a separate line?
contact@brighttrimyard.com.au
www.brighttrimyard.com.au
ABN: 38 916 204 571
Cards are to be generic and not have a persons name or title, only a business card for the business itself.
Will consider ideas or suggestions from designers - maybe a full size logo, maybe a special offer for "refer a friend who makes a booking and receive 25% off your next service" or similar, maybe both logo and text at bottom with refer a friend offer.

```html
<!DOCTYPE html>
<html lang="en">
<head>
<meta charset="utf-8">
<title>Bright Trim Yard – Business Cards</title>
<link rel="stylesheet" href="https://fonts.googleapis.com/css2?family=Nunito:wght@400;600;700;800&display=swap">
<style>
  :root {
    --bg: #e9e7e3;
    --card: #ffffff;
    --blue: #29a8e0;
    --orange: #f39a1e;
    --green: #7bbb2f;
    --ink: #2b8fc4;
    --text: #6a6a6a;
    --rule: #d4d4d4;
  }
  * { box-sizing: border-box; margin: 0; padding: 0; }
  html, body { width: 1200px; height: 871px; overflow: hidden; }
  body {
    background: var(--bg);
    font-family: "Nunito", sans-serif;
    display: flex;
    align-items: center;
    justify-content: center;
    gap: 40px;
  }
  .card {
    position: relative;
    width: 540px;
    height: 310px;
    background: var(--card);
    border-radius: 18px;
    overflow: hidden;
    box-shadow: 0 6px 18px rgba(0,0,0,.18);
  }
  .brand {
    display: flex;
    align-items: center;
    justify-content: center;
    gap: 10px;
  }
  .brand-dot {
    width: 18px; height: 18px; border-radius: 50%;
    background: var(--blue);
  }
  .brand-name {
    font-weight: 800;
    font-size: 44px;
    color: var(--blue);
    letter-spacing: -0.5px;
    line-height: 1;
  }
  .tagline {
    text-align: center;
    font-weight: 700;
    color: var(--ink);
    font-size: 19px;
    margin-top: 6px;
  }

  /* Offer side */
  .card--offer .brand { margin-top: 70px; }
  .offer {
    position: absolute;
    left: 30px; right: 30px; bottom: 62px;
    display: flex;
    align-items: center;
    justify-content: center;
    gap: 16px;
    color: var(--ink);
    font-weight: 600;
    font-size: 17px;
    line-height: 1.2;
  }
  .offer-text { text-align: right; }
  .offer-tail { text-align: left; color: var(--green); }
  .offer-badge {
    flex: none;
    width: 74px; height: 74px; border-radius: 50%;
    background: radial-gradient(circle at 35% 30%, #ffc15a, var(--orange));
    color: #fff;
    font-weight: 800;
    font-size: 20px;
    line-height: .95;
    display: flex; flex-direction: column;
    align-items: center; justify-content: center;
  }
  .offer-badge small { font-size: 13px; font-weight: 700; }

  /* Contact side */
  .card--contact .brand { margin-top: 42px; }
  .details {
    position: absolute;
    top: 148px; left: 0; right: 0;
    display: flex;
    justify-content: center;
    font-size: 13px;
    color: var(--text);
    line-height: 1.45;
  }
  .details-left {
    text-align: right;
    padding-right: 18px;
    border-right: 1px solid var(--rule);
  }
  .details-left .abn { margin-bottom: 10px; }
  .details-right { padding-left: 18px; }
  .contact-line { display: flex; align-items: center; gap: 7px; }
  .contact-line svg { width: 13px; height: 13px; fill: var(--text); flex: none; }

  .band {
    position: absolute;
    left: 0; right: 0; bottom: 0;
    height: 50px;
    display: flex;
  }
  .band-clean { width: 96px; background: var(--blue); position: relative; }
  .band-fix {
    flex: 1; background: var(--orange);
    display: flex; align-items: center; justify-content: space-between;
    padding: 0 18px 0 22px;
    color: #fff; font-weight: 700; font-size: 15px;
  }
  .band-mow { width: 96px; background: var(--green); position: relative; }
  .band-icon {
    display: block;
    width: 28px; height: 28px; border-radius: 6px;
    background: rgba(255,255,255,.35);
  }
  .band-clean .band-icon, .band-mow .band-icon {
    position: absolute; left: 50%; top: 50%;
    transform: translate(-50%, -50%);
  }
</style>
</head>
<body>

  <section class="card card--offer">
    <div class="brand">
      <span class="brand-dot"></span>
      <span class="brand-name">Bright Trim Yard</span>
    </div>
    <p class="tagline">We Scrub. We Mend. We Cut.</p>
    <div class="offer">
      <p class="offer-text">Refer a friend who makes<br>a booking and receive</p>
      <div class="offer-badge">25%<small>off</small></div>
      <p class="offer-tail">your next<br>service</p>
    </div>
  </section>

  <section class="card card--contact">
    <div class="brand">
      <span class="brand-dot"></span>
      <span class="brand-name">Bright Trim Yard</span>
    </div>
    <p class="tagline">We Scrub. We Mend. We Cut.</p>

    <div class="details">
      <div class="details-left">
        <p class="abn">ABN: 38 916 204 571</p>
        <p>PO Box 318</p>
        <p>Galloway Rise, QLD, 4127</p>
      </div>
      <div class="details-right">
        <p class="contact-line">
          <svg viewBox="0 0 24 24"><path d="M6.6 10.8a15.1 15.1 0 0 0 6.6 6.6l2.2-2.2a1 1 0 0 1 1-.25 11.4 11.4 0 0 0 3.6.57 1 1 0 0 1 1 1V20a1 1 0 0 1-1 1A17 17 0 0 1 3 4a1 1 0 0 1 1-1h3.5a1 1 0 0 1 1 1c0 1.250.2 2.45.57 3.57a1 1 0 0 1-.25 1z"/></svg>
          0412 GO TIDY
        </p>
        <p class="contact-line">
          <svg viewBox="0 0 24 24"><path d="M6.6 10.8a15.1 15.1 0 0 0 6.6 6.6l2.2-2.2a1 1 0 0 1 1-.25 11.4 11.4 0 0 0 3.6.57 1 1 0 0 1 1 1V20a1 1 0 0 1-1 1A17 17 0 0 1 3 4a1 1 0 0 1 1-1h3.5a1 1 0 0 1 1 1c0 1.250.2 2.45.57 3.57a1 1 0 0 1-.25 1z"/></svg>
          0412 46 8439
        </p>
        <p class="contact-line">
          <svg viewBox="0 0 24 24"><path d="M2 5h20v14H2zm2 2v.5l8 5 8-5V7zm0 2.8V17h16V9.8l-8 5z"/></svg>
          contact@brighttrimyard.com.au
        </p>
      </div>
    </div>

    <div class="band">
      <div class="band-clean"><span class="band-icon" role="img" aria-label="Soap bubbles symbol for cleaning"></span></div>
      <div class="band-fix">
        <span>www.brighttrimyard.com.au</span>
        <span class="band-icon" role="img" aria-label="Wrench symbol for repairs"></span>
      </div>
      <div class="band-mow"><span class="band-icon" role="img" aria-label="Leaf symbol for mowing and gardens"></span></div>
    </div>
  </section>

</body>
</html>
```